Thank You For Shopping / Hair Care Tips

I need “Thank You For Shopping”
Post cards made for my hair business !
I added pictures of post cards that I really like . I also added my LuzeKora Wigs logo for you guys to use

I want the backside of the flyer to have hair care tips !
I want people to have full directions on how to care for their wigs

Target Market(s)

Im marking to young woman to older middle aged woman
Ages 23-66 . I want my flyer to look mature And classy

Industry/Entity Type

Hair And Beauty

Font styles to use
Serif
Script

Colors
e34699
e34298
e34398

Requirements
Must have
• The flyer must have the Instagram logo with my Instagram name next to it @luze.kora.wigs__
• Also it must have my “Luze Kora Wigs” logo that I’ve uploaded in the pictures section .
• Flyer had to be two sides . One side “ thank you for shopping “ side two “hair care tips”
• My website must be on the flyer - www.luzekorawigs.example
• The flyer must match the colors of my logo
• All white . With the pink and glitter sliver you see on my logo
Nice to have
• Nice to have a glitter border
Should not have
• The flyer should not have different colors that don’t match my logo
• It shouldn’t be made without having my Instagram or website on the flyer

```html
<!DOCTYPE html>
<html lang="en">
<head>
<meta charset="utf-8">
<title>Luze Kora Wigs – Thank You Postcard</title>
<link href="https://fonts.googleapis.com/css2?family=Damion&family=Montserrat:wght@400;500&display=swap" rel="stylesheet">
<style>
  :root {
    --backdrop: #e08c8e;
    --card: #edece7;
    --pink: #c4458f;
    --grey: #8a8a85;
    --text-grey: #7b7b76;
    --frame: #8d8d8d;
    --white: #f4f3ef;
  }
  * { box-sizing: border-box; margin: 0; padding: 0; }
  html, body { width: 1200px; height: 1200px; overflow: hidden; }
  body {
    background: var(--backdrop);
    font-family: "Montserrat", Arial, sans-serif;
    position: relative;
  }
  .postcard {
    position: absolute;
    left: 231px;
    width: 749px;
    height: 498px;
    background: var(--card);
    border: 7px solid var(--frame);
    outline: 1px solid #b9b9b9;
    outline-offset: -5px;
    box-shadow: 10px 10px 12px rgba(80, 40, 40, 0.45);
    overflow: hidden;
  }
  .postcard--front { top: 55px; }
  .postcard--back { top: 605px; }

  .script-title {
    position: absolute;
    left: 0; right: 0;
    text-align: center;
    font-family: "Damion", cursive;
    color: var(--pink);
    line-height: 1;
  }
  .postcard--front .script-title { top: 30px; font-size: 132px; }
  .postcard--back .script-title { top: 16px; font-size: 112px; }

  .purchase-band {
    position: absolute;
    left: 0; right: 0;
    top: 176px;
    height: 90px;
    background: var(--pink);
    border-top: 9px solid var(--grey);
    border-bottom: 8px solid var(--grey);
    color: var(--white);
    font-size: 50px;
    font-weight: 500;
    letter-spacing: 1px;
    display: flex;
    align-items: center;
    justify-content: center;
  }

  .brand-name {
    position: absolute;
    left: 22px;
    top: 318px;
    width: 180px;
    color: var(--pink);
    font-size: 30px;
    font-weight: 500;
    line-height: 1.15;
    text-align: center;
  }

  .social-handle {
    position: absolute;
    left: 415px;
    top: 296px;
    display: flex;
    align-items: center;
    gap: 14px;
    color: var(--text-grey);
    font-size: 29px;
    font-weight: 500;
  }
  .social-handle .marker {
    width: 26px; height: 26px;
    border: 2px solid #e86ad6;
    border-radius: 5px;
  }

  .website {
    position: absolute;
    left: 0; right: 0;
    bottom: 6px;
    text-align: center;
    color: var(--text-grey);
    font-size: 25px;
    font-weight: 500;
  }

  .care-text {
    position: absolute;
    left: 55px;
    top: 160px;
    width: 630px;
    color: var(--text-grey);
    font-size: 18.5px;
    font-weight: 500;
    line-height: 23px;
    text-align: center;
  }
  .care-text .portrait-area {
    float: left;
    width: 140px;
    height: 165px;
    margin: 30px 12px 0 -15px;
    border-radius: 45% 45% 40% 40%;
    background: radial-gradient(circle at 55% 45%, #e6c6d8 0 22%, var(--pink) 23%);
  }
</style>
</head>
<body>
  <section class="postcard postcard--front">
    <h1 class="script-title">Thank You</h1>
    <div class="purchase-band">FOR YOUR PURCHASE</div>
    <div class="brand-name">Luze Kora Wigs</div>
    <div class="social-handle"><span class="marker"></span>@luze.kora.wigs__</div>
    <p class="website">www.luzekorawigs.example</p>
  </section>

  <section class="postcard postcard--back">
    <h2 class="script-title">Hair Care Tips</h2>
    <p class="care-text">
      <span class="portrait-area" role="img" aria-label="Pink illustration of a woman with long wavy hair"></span>
      Lorem ipsum dolor sit amet, consectetuer adipiscing elit, sed diam nonummy nibh euismod tincidunt ut laoreet dolore magna aliquam erat volutpat. Ut wisi enim ad minim veniam, quis nostrud exerci tation ullamcorper suscipit lobortis nisl ut aliquip ex ea commodo consequat. Duis autem vel eum iriure dolor in hendrerit in vulputate velit esse molestie consequat, vel illum dolore eu feugiat nulla facilisis at vero eros et accumsan et iusto odio dignissim qui blandit praesent luptatum zzril delenit augue duis dolore te feugait nulla facilisi.
    </p>
    <p class="website">www.luzekorawigs.example</p>
  </section>
</body>
</html>
```